Business Cards for a small business advisory (business services)

Professional look. Same as would apply for a lawyer, accountant, or other financial services professional. Please use the logo colors

Target Market(s)

small business owners

Industry/Entity Type

Financial Servics

Contact Information for Business Card

Name: Glenn R. Whitaker, CAIA / Title: Business Advisor / Office #: (555) 284-7193 / Mobile #: (555) 903-6418 / Email: g.whitaker@ambervalebusinessbrokers.example / Web: www.ambervalebusinessbrokers.example

Font styles to use
Sans Serif

```html
<!DOCTYPE html>
<html lang="en">
<head>
<meta charset="utf-8">
<title>Ambervale Business Brokers &amp; Advisors – Business Cards</title>
<link rel="stylesheet" href="https://fonts.googleapis.com/css2?family=Montserrat:wght@700&family=Open+Sans:wght@400;700&display=swap">
<style>
  :root {
    --navy: #17366b;
    --navy-deep: #1a3868;
    --navy-emboss: #24467f;
    --green: #86c440;
    --ink: #222831;
    --paper: #ffffff;
    --backdrop: #3a3a3a;
  }
  * { box-sizing: border-box; margin: 0; padding: 0; }
  html, body { width: 1200px; height: 780px; overflow: hidden; }
  body {
    background: var(--backdrop);
    font-family: "Open Sans", Arial, sans-serif;
    position: relative;
  }
  .card {
    position: absolute;
    top: 240px;
    width: 525px;
    height: 300px;
    border-radius: 22px;
    overflow: hidden;
  }
  .card--front { left: 50px; background: var(--paper); }
  .card--back  { left: 625px; background: var(--navy-deep); }

  .brand {
    position: absolute;
    display: flex;
    align-items: center;
    gap: 12px;
    font-family: "Montserrat", Arial, sans-serif;
    font-weight: 700;
    line-height: 1;
  }
  .brand__dot { width: 34px; height: 34px; border-radius: 50%; flex: none; }
  .brand__name { display: flex; flex-direction: column; gap: 6px; }
  .brand__word { font-size: 40px; letter-spacing: -0.5px; }
  .brand__desc { font-size: 12.5px; letter-spacing: 1.6px; text-transform: uppercase; }

  .card--front .brand { top: 30px; left: 150px; color: var(--navy); }
  .card--front .brand__dot { background: var(--navy); }

  .card--back .brand {
    top: 50%; left: 50%; transform: translate(-50%, -50%);
    color: var(--navy-emboss);
  }
  .card--back .brand__dot { background: var(--navy-emboss); }
  .card--back .brand__word { font-size: 54px; }
  .card--back .brand__desc { font-size: 15px; }

  .holder { position: absolute; top: 118px; left: 0; width: 100%; }
  .holder__bar {
    position: absolute; left: 0; top: 2px;
    width: 14px; height: 44px; background: var(--green);
  }
  .holder__name {
    margin-left: 36px;
    font-family: "Montserrat", Arial, sans-serif;
    font-weight: 700; font-size: 21px; color: var(--navy);
  }
  .holder__title {
    display: flex; align-items: center; gap: 8px;
    margin-left: 36px; margin-top: 2px;
    font-size: 13px; color: var(--green);
  }
  .holder__rule { flex: 1; height: 1.5px; background: var(--green); margin-right: 40px; }

  .contacts {
    position: absolute; top: 188px; left: 36px;
    list-style: none; font-size: 12.5px; color: var(--ink);
  }
  .contacts li { display: flex; align-items: center; gap: 7px; height: 19px; }
  .contacts svg { width: 11px; height: 11px; fill: var(--navy); flex: none; }
</style>
</head>
<body>

<section class="card card--front" aria-label="Business card front">
  <div class="brand">
    <span class="brand__dot"></span>
    <span class="brand__name">
      <span class="brand__word">Ambervale</span>
      <span class="brand__desc">Business Brokers &amp; Advisors</span>
    </span>
  </div>

  <div class="holder">
    <span class="holder__bar"></span>
    <p class="holder__name">Glenn R. Whitaker, CAIA</p>
    <p class="holder__title">Business Advisor <span class="holder__rule"></span></p>
  </div>

  <ul class="contacts">
    <li>
      <svg viewBox="0 0 24 24" aria-hidden="true"><path d="M6.6 10.8a15 15 0 0 0 6.6 6.6l2.2-2.2c.3-.3.7-.4 1-.2 1.1.4 2.3.6 3.6.6.6 0 1 .4 1 1V20c0 .6-.4 1-1 1A17 17 0 0 1 3 4c0-.6.4-1 1-1h3.5c.6 0 1 .4 1 1 0 1.3.2 2.5.6 3.6.1.3 0 .7-.2 1z"/></svg>
      (555) 284-7193
    </li>
    <li>
      <svg viewBox="0 0 24 24" aria-hidden="true"><path d="M7 1h10a2 2 0 0 1 2 2v18a2 2 0 0 1-2 2H7a2 2 0 0 1-2-2V3a2 2 0 0 1 2-2zm0 3v14h10V4zm5 15.2a1.2 1.2 0 1 0 0 2.4 1.2 1.2 0 0 0 0-2.4z"/></svg>
      (555) 903-6418
    </li>
    <li>
      <svg viewBox="0 0 24 24" aria-hidden="true"><path d="M2 5h20v14H2zm2 2v.5l8 5 8-5V7zm0 2.9V17h16V9.9l-8 5z"/></svg>
      g.whitaker@ambervalebusinessbrokers.example
    </li>
    <li>
      <svg viewBox="0 0 24 24" aria-hidden="true"><path d="M12 2a10 10 0 1 0 0 20 10 10 0 0 0 0-20zm6.9 6h-2.9a15 15 0 0 0-1.3-3.9A8 8 0 0 1 18.9 8zM12 4c.8 1.2 1.5 2.5 1.9 4h-3.8c.4-1.5 1.1-2.8 1.9-4zM4.3 14a8 8 0 0 1 0-4h3.4a16 16 0 0 0 0 4zm.8 2h2.9c.3 1.4.8 2.7 1.3 3.9A8 8 0 0 1 5.1 16zM8 8H5.1a8 8 0 0 1 4.2-3.9C8.8 5.3 8.3 6.6 8 8zm4 12c-.8-1.2-1.5-2.5-1.9-4h3.8c-.4 1.5-1.1 2.8-1.9 4zm2.3-6H9.7a14 14 0 0 1 0-4h4.6a14 14 0 0 1 0 4zm.4 5.9c.5-1.2 1-2.5 1.3-3.9h2.9a8 8 0 0 1-4.2 3.9zm1.6-5.9a16 16 0 0 0 0-4h3.4a8 8 0 0 1 0 4z"/></svg>
      www.ambervalebusinessbrokers.example
    </li>
  </ul>
</section>

<section class="card card--back" aria-label="Business card back">
  <div class="brand">
    <span class="brand__dot"></span>
    <span class="brand__name">
      <span class="brand__word">Ambervale</span>
      <span class="brand__desc">Business Brokers &amp; Advisors</span>
    </span>
  </div>
</section>

</body>
</html>
```